Design a Flyer/Poster for a Mountain Adventure Event

We need a flyer designed to be printed on 8.5" x 11" paper to advertise an event entitled Cobalt Quest 2014. The copy has already been written. The end result will need to be delivered in a fully editable format (Adobe Illustrator or other Adobe product is preferred). All components of the final deliverable file must be easily editable with appropriate software, as details of this event may change before printing. The final deliverable must also be in a high resolution (min 300dpi) for glossy printing at 8.5" x 11" printed size.

This event is still in concept phase, and the website does not yet exist. Ideas for images are attached below - I do not have rights to use those particular images. In addition to the photo ideas, I have attached versions of the logo for the organization that will benefit from the event (Center for Pellam & Orrin Inquiry). One of those logos will need to be used (probably towards bottom of flyer/poster) with the text: Benefiting the Center for Pellam & Orrin Inquiry

Text for Flyer/Poster:
Cobalt Quest 2014
June 15 - 30

1. Run/Hike in the Mountains between June 15-30, 2014
2. Track it with GPS or Satellite
3. Follow your Competitors online

Compete for:
Most Elevation Gain
Most Miles
Most Summits
Best Photos
Best Family Adventures

Prizes awarded by Age Class, Gender, Individuals & Teams
You could win $1,000!

Where:
Mountains of your Choice

Registration: $99 (Limited to 500 Participants)
Optional: Rent a Trava K7TM with Unlimited Tracking: $99

Benefiting the Center for Pellam & Orrin Inquiry

```html
<!DOCTYPE html>
<html lang="en">
<head>
<meta charset="utf-8">
<title>Cobalt Quest 2014</title>
<link rel="stylesheet" href="https://fonts.googleapis.com/css2?family=Permanent+Marker&family=Kalam:wght@400;700&display=swap">
<style>
  :root {
    --sky-top: #3f8fc9;
    --sky-mid: #8cc2e6;
    --snow: #dfe9f1;
    --rock: #5c6f82;
    --shadow: #101418;
    --ink: #111111;
    --white: #ffffff;
    --magenta: #c8238d;
    --yellow: #f4ea1c;
    --blue: #1b86c8;
    --orange: #ea8a22;
    --green: #7cb23a;
    --pink: #b92a86;
    --purple: #6a3f8e;
    --banner: #e1257f;
  }
  * { margin: 0; padding: 0; box-sizing: border-box; }
  html, body { width: 1200px; height: 927px; overflow: hidden; background: var(--shadow); }
  .poster {
    position: relative;
    width: 1200px;
    height: 927px;
    overflow: hidden;
    font-family: "Kalam", cursive;
    color: var(--white);
  }
  .scene {
    position: absolute;
    inset: 0;
    background:
      radial-gradient(ellipse 55% 40% at 88% 90%, var(--shadow) 0%, rgba(16,20,24,0.85) 55%, rgba(16,20,24,0) 100%),
      radial-gradient(ellipse 45% 25% at 40% 36%, var(--snow) 0%, rgba(223,233,241,0.5) 50%, rgba(223,233,241,0) 100%),
      linear-gradient(180deg, var(--sky-top) 0%, var(--sky-mid) 22%, var(--rock) 45%, var(--snow) 72%, #3a4550 88%, var(--shadow) 100%);
  }
  .title {
    position: absolute;
    left: 26px;
    top: 38px;
    font-family: "Permanent Marker", cursive;
    font-size: 78px;
    letter-spacing: 3px;
    color: var(--ink);
    line-height: 1;
  }
  .title-year {
    position: absolute;
    left: 625px;
    top: 150px;
    font-family: "Permanent Marker", cursive;
    font-size: 86px;
    color: var(--ink);
    line-height: 1;
    letter-spacing: 2px;
  }
  .dates {
    position: absolute;
    left: 662px;
    top: 240px;
    font-family: "Permanent Marker", cursive;
    font-size: 30px;
    color: var(--magenta);
    letter-spacing: 1px;
  }
  .steps {
    position: absolute;
    left: 27px;
    top: 350px;
    list-style: none;
    font-size: 19px;
    font-style: italic;
    line-height: 1.15;
  }
  .compete-heading {
    position: absolute;
    left: 486px;
    top: 466px;
    font-family: "Permanent Marker", cursive;
    font-size: 38px;
    color: var(--yellow);
  }
  .categories {
    position: absolute;
    left: 0;
    top: 533px;
    width: 1200px;
    height: 123px;
    display: flex;
    gap: 2px;
  }
  .category {
    flex: 1;
    display: flex;
    align-items: center;
    justify-content: center;
    text-align: center;
    font-family: "Permanent Marker", cursive;
    font-size: 30px;
    line-height: 1.05;
    padding: 0 8px;
  }
  .category--elevation { background: var(--blue); }
  .category--miles { background: var(--orange); }
  .category--summits { background: var(--green); }
  .category--photos { background: var(--pink); }
  .category--family { background: var(--purple); }
  .details {
    position: absolute;
    right: 36px;
    top: 688px;
    text-align: right;
    font-style: italic;
    font-size: 16px;
    line-height: 1.4;
  }
  .details .where { margin-bottom: 18px; }
  .prize-banner {
    position: absolute;
    left: 14px;
    top: 738px;
    width: 490px;
    height: 128px;
    transform: rotate(-4deg);
  }
  .prize-banner svg { position: absolute; inset: 0; }
  .prize-copy {
    position: absolute;
    inset: 0;
    text-align: center;
    padding-top: 18px;
  }
  .prize-copy .awards { font-style: italic; font-size: 16px; }
  .prize-copy .headline {
    font-family: "Permanent Marker", cursive;
    font-size: 40px;
    color: var(--yellow);
    line-height: 1.1;
  }
  .prize-copy .site { font-style: italic; font-size: 16px; padding-left: 180px; }
  .org {
    position: absolute;
    left: 940px;
    top: 848px;
    display: flex;
    align-items: center;
    gap: 10px;
  }
  .org-mark {
    width: 52px;
    height: 52px;
    border-radius: 50%;
    background: var(--blue);
    flex: none;
  }
  .org-name {
    font-family: "Kalam", cursive;
    font-weight: 700;
    font-size: 14px;
    line-height: 1.1;
    text-transform: uppercase;
    color: var(--white);
    width: 150px;
  }
</style>
</head>
<body>
<main class="poster">
  <div class="scene" role="img" aria-label="Snowy mountain range under a blue sky, with a hiker standing arms raised on a dark summit at the right"></div>

  <h1 class="title">Cobalt Quest</h1>
  <div class="title-year">2014</div>
  <div class="dates">June 15-30</div>

  <ol class="steps">
    <li>1. Run/Hike in the Mountains between June 15-30, 2014</li>
    <li>2. Track it with GPS or Satellite</li>
    <li>3. Follow your Competitors online</li>
  </ol>

  <h2 class="compete-heading">Compete for:</h2>
  <div class="categories">
    <div class="category category--elevation">Most<br>Elevation Gain</div>
    <div class="category category--miles">Most Miles</div>
    <div class="category category--summits">Most<br>Summits</div>
    <div class="category category--photos">Best Photos</div>
    <div class="category category--family">Best Family<br>Adventures</div>
  </div>

  <div class="details">
    <p class="where">Where:<br>Mountains of your Choice</p>
    <p>Registration: $99 (Limited to 500 Participants)<br>Optional: Rent a Trava K7TM with Unlimited Tracking: $99</p>
  </div>

  <div class="prize-banner">
    <svg width="490" height="128" viewBox="0 0 490 128" aria-hidden="true">
      <path d="M6 14 L484 2 L488 118 L2 126 Z" fill="var(--banner)"/>
    </svg>
    <div class="prize-copy">
      <p class="awards">Prizes awarded by Age Class, Gender, Individuals &amp; Teams</p>
      <p class="headline">You could win $1,000!</p>
      <p class="site">CobaltQuest2014.com</p>
    </div>
  </div>

  <div class="org">
    <span class="org-mark"></span>
    <span class="org-name">Center for Pellam &amp; Orrin Inquiry</span>
  </div>
</main>
</body>
</html>
```